STRIDE AND SHINE 1K/5K WALK/RUN HEALTH EXPO

NEED A HEALTH FAIR FLYER EMPHASIZING THE WALK AS WELL AS ALL HEALTH FAIR. MY VISION IS TO HAVE SOMEONE RUNNING WITH VARIOUS HEALTH CONDITIONS INSIDE THE BRAIN . AS MANY HEALTH CONDITIONS AS POSSIBLE SUCH AS HEART DISEASE, DIABETES, MENTAL HEALTH, AND AS MANY THAT CAN FIT IN THE BRAIN. THE HAIR CAN ALSO HAVE THE COLORS THAT REPRESENT THE HEALTH CONDITION. Eg. Pink represents breast cancer; red represent heart disease, mental Health is green
Details: Corvel Alumnae Chapter 1k/5k Health Expo
Date: 3/25/2023
Time: 8am - 1:00 PM (8am Check in/ Walk Starts at 9:00
Location: Pellbrook Park, Ravelford TX
Theme: Stride and Shine (We are bringing awareness to all health issues that are affecting our community
We would like everyone to wear the color in which they would like to bring awareness to. Eg. Pink for Breast Cancer
Green for Mental Health.)
Agenda: 8am Checkin
9am walk starts
10am-12 Music, Food, Fun, Prizes and Health Experts from the community : Working on Special Guest: Tuck Buck to lead the walk: Trying to get the Ravelford Cheerleaders
12-1: Closing Ceremony and Breakdown

```html
<!DOCTYPE html>
<html lang="en">
<head>
<meta charset="utf-8">
<title>Stride and Shine – Corvel Alumnae Chapter 1K/5K Health Expo</title>
<link rel="stylesheet" href="https://fonts.googleapis.com/css2?family=Bebas+Neue&family=Barlow+Condensed:ital,wght@1,900&family=Poppins:wght@500;600&display=swap">
<style>
  :root {
    --page-black: #232323;
    --sun-yellow: #f4ec33;
    --teal: #527e79;
    --paper: #f4f4f6;
    --ink: #2d2d2d;
    --deep-plum: #2a1a33;
    --chapter-red: #9b1c1f;
    --health-green: #2e9b34;
    --agenda-grey: #c3cfca;
    --pin-blue: #2f86c8;
    --white: #ffffff;
  }
  * { margin: 0; padding: 0; box-sizing: border-box; }
  html, body { width: 1200px; height: 1200px; overflow: hidden; background: var(--page-black); }
  .flyer { position: relative; width: 1200px; height: 1200px; background: var(--page-black); overflow: hidden; }
  .sheet { position: absolute; left: 137px; top: 0; width: 926px; height: 1200px; background: var(--paper); overflow: hidden; }
  .sheet > * { position: absolute; }

  .header-band { left: 0; top: 0; width: 926px; height: 218px; background: var(--sun-yellow); }
  .chapter-mark { left: 80px; top: 78px; width: 250px; display: flex; align-items: center; gap: 10px;
    font-family: "Poppins", sans-serif; font-weight: 600; font-size: 19px; line-height: 1.15; color: var(--chapter-red); text-transform: uppercase; }
  .chapter-mark .dot { width: 22px; height: 22px; border-radius: 50%; background: var(--chapter-red); flex: none; }
  .headline { left: 334px; top: 44px; font-family: "Bebas Neue", sans-serif; font-size: 94px; line-height: 73px; color: var(--ink); white-space: nowrap; }
  .headline .walk { color: var(--chapter-red); }
  .headline .fair { color: var(--health-green); }

  .teal-field { left: 0; top: 218px; width: 926px; height: 600px; }
  .brain-art { left: 83px; top: 276px; width: 382px; height: 426px; border-radius: 40% 40% 30% 30%;
    background: radial-gradient(ellipse at 50% 35%, #f6a7a4 0%, #ec8f8d 55%, rgba(82,126,121,0) 72%); }
  .theme-title { left: 484px; top: 262px; font-family: "Barlow Condensed", sans-serif; font-style: italic; font-weight: 900;
    font-size: 124px; line-height: 113px; letter-spacing: -2px; color: var(--white); white-space: nowrap; }
  .theme-title .and { color: var(--deep-plum); }
  .expo-line { left: 484px; top: 618px; font-family: "Bebas Neue", sans-serif; font-size: 38px; line-height: 1; color: var(--sun-yellow); letter-spacing: 0.5px; white-space: nowrap; }

  .details { right: 480px; top: 812px; text-align: right; font-family: "Poppins", sans-serif; color: #111; white-space: nowrap; }
  .details .time { font-weight: 600; font-size: 24px; line-height: 30px; }
  .details .checkin { font-weight: 500; font-size: 19px; line-height: 27px; }
  .details .place { font-weight: 600; font-size: 21px; line-height: 32px; display: flex; align-items: center; justify-content: flex-end; gap: 4px; }
  .agenda-label { left: 276px; top: 904px; width: 170px; height: 31px; background: var(--sun-yellow);
    font-family: "Poppins", sans-serif; font-weight: 600; font-size: 20px; line-height: 31px; text-align: right; padding-right: 16px; color: #111; }
  .agenda-list { left: 68px; top: 941px; width: 375px; height: 166px; background: var(--agenda-grey); list-style: none;
    padding: 7px 12px 0 0; text-align: right; font-family: "Poppins", sans-serif; font-weight: 500; font-size: 16.8px; line-height: 18.7px; color: #1a1a1a; white-space: nowrap; }

  .brain-wave { left: 745px; top: 779px; width: 136px; height: 125px; border-radius: 40%;
    background: radial-gradient(ellipse at 50% 40%, #f3a09d 0%, #e98987 55%, rgba(244,244,246,0) 72%); }
  .chapter-stack { left: 490px; top: 802px; font-family: "Bebas Neue", sans-serif; font-size: 118px; line-height: 94px; color: #141414; white-space: nowrap; }
  .dotted-rule { left: 490px; top: 1011px; width: 340px; height: 8px;
    background-image: radial-gradient(circle, #141414 0 2.6px, transparent 3px); background-size: 12.4px 8px; }
  .event-date { left: 488px; top: 1028px; font-family: "Bebas Neue", sans-serif; font-size: 108px; line-height: 96px; letter-spacing: -1px; color: #141414; white-space: nowrap; }

  .posted-bar { left: 68px; top: 1137px; width: 412px; height: 63px; background: var(--sun-yellow);
    font-family: "Poppins", sans-serif; font-weight: 600; font-size: 22px; line-height: 63px; text-align: center; color: #111; white-space: nowrap; }
  .posted-bar span { color: var(--chapter-red); }
  .slogan-bar { left: 480px; top: 1137px; width: 364px; height: 63px; background: var(--chapter-red);
    font-family: "Bebas Neue", sans-serif; font-size: 38px; line-height: 66px; text-align: center; color: var(--white); letter-spacing: 1px; white-space: nowrap; }
</style>
</head>
<body>
<main class="flyer">
  <section class="sheet">
    <div class="header-band"></div>
    <div class="chapter-mark"><span class="dot"></span><span>Corvel Alumnae Chapter</span></div>
    <h1 class="headline"><span class="walk">WALK</span> AS WELL AS<br>ALL <span class="fair">HEALTH FAIR</span></h1>

    <svg class="teal-field" width="926" height="600" viewBox="0 0 926 600">
      <polygon points="0,0 926,0 926,434 0,593" fill="var(--teal)"/>
    </svg>
    <div class="brain-art" role="img" aria-label="Cartoon brain character with legs and sneakers, its top filled with health condition words such as mental health, heart disease, diabetes, cancer and anxiety"></div>
    <h2 class="theme-title">STRIDE<br><span class="and">AND</span><br>SHINE</h2>
    <p class="expo-line">CHAPTER 1K/5K HEALTH EXPO</p>

    <div class="details">
      <p class="time">Time: 8am - 1:00 PM</p>
      <p class="checkin">(8am Check in/ Walk Starts at 9:00)</p>
      <p class="place">Pellbrook Park, Ravelford TX
        <svg width="18" height="24" viewBox="0 0 18 24" aria-hidden="true"><path d="M9 0C4 0 0 4 0 9c0 6.5 9 15 9 15s9-8.5 9-15C18 4 14 0 9 0z" fill="var(--pin-blue)"/><circle cx="9" cy="9" r="3.3" fill="#fff"/></svg>
      </p>
    </div>
    <p class="agenda-label">Agenda:</p>
    <ul class="agenda-list">
      <li>8am Checkin</li>
      <li>9am walk starts</li>
      <li>10am-12 Music, Food, Fun, Prizes and</li>
      <li>Health Experts from the community</li>
      <li>Working on Special Guest:</li>
      <li>Tuck Buck to lead the walk:</li>
      <li>Trying to get the Ravelford Cheerleaders</li>
      <li>12-1: Closing Ceremony and Breakdown</li>
    </ul>

    <div class="brain-wave" role="img" aria-label="Small cartoon brain character waving"></div>
    <p class="chapter-stack">CORVEL<br>ALUMNAE</p>
    <div class="dotted-rule"></div>
    <p class="event-date">3/25/2023</p>

    <p class="posted-bar">Added <span>Friday, 23 December 2022</span></p>
    <p class="slogan-bar">YOUR BRAIN IS A CHAMPION</p>
  </section>
</main>
</body>
</html>
```